Appealing productlabel for jar with toffees

I run a small import company within confectionary (candy, chocolate, toffees and so on). We are planning launching a series of bulk product - and would like to start up with this article enclosed.<br/>Packaging: Transparent plastic Jar with black lid. Height 22 cm, diameter 15 cm.<br/>I was thinking about a label with the dimensions 10,5 x 14,8 cm. since a have a label sheet in this format (I will probably end up getting it printed at a professional printing company)<br/>Unique Selling Points: Great Toffees with great taste. The toffees do NOT stick to your teeth, 1000 gram, hygienically wrapped.<br/>Brand Name RENO<br/><br/>Buyers/ Clients: Office Supplies

Target Market(s)

Adult professional purchasers within the segmment: Office Supply, Food Service

Font styles to use
Serif

Requirements
Must have
• Appealing, catchy, attractive design
Nice to have
• Surprise me :-)
Should not have
• A traditional candy design which is appealing to kids - the clients will be grown-ups

```html
<!DOCTYPE html>
<html lang="da">
<head>
<meta charset="utf-8">
<title>Karameller med Havsalt – etiket</title>
<link rel="stylesheet" href="https://fonts.googleapis.com/css2?family=Playfair+Display:wght@900&family=Yellowtail&family=Montserrat:ital,wght@0,400;1,400;0,800&display=swap">
<style>
  :root {
    --page: #f7f7f7;
    --paper: #ffffff;
    --sun: #fdc800;
    --sun-deep: #f5b400;
    --ink: #000000;
    --mint: #a8e4c6;
    --white: #ffffff;
    --pastel-a: #fdf4f6;
    --pastel-b: #f1f8fc;
    --mark-light: rgba(120, 110, 110, 0.22);
    --mark-dark: rgba(150, 110, 0, 0.25);
  }
  * { box-sizing: border-box; margin: 0; padding: 0; }
  html, body { width: 886px; height: 1200px; overflow: hidden; background: var(--page); }
  .canvas { position: relative; width: 886px; height: 1200px; }
  .label {
    position: absolute; left: 79px; width: 727px; height: 516px;
    box-shadow: 0 6px 28px rgba(0,0,0,0.12);
    overflow: hidden;
  }
  .label--light { top: 62px; }
  .label--sun { top: 615px; }
  .label svg { display: block; width: 727px; height: 516px; }
  .brand { font-family: "Montserrat", sans-serif; font-weight: 800; font-size: 19px; letter-spacing: 1px; fill: var(--white); }
  .tagline { font-family: "Montserrat", sans-serif; font-style: italic; font-size: 13.5px; letter-spacing: 0.6px; fill: var(--white); }
  .title { font-family: "Playfair Display", serif; font-weight: 900; font-size: 38px; letter-spacing: 2px; fill: var(--mint); }
  .script { font-family: "Yellowtail", cursive; font-size: 42px; fill: var(--mint); }
  .copy { font-family: "Montserrat", sans-serif; font-size: 10.5px; letter-spacing: 0.4px; fill: var(--white); }
  .corner-mark { font-family: "Montserrat", sans-serif; font-weight: 800; font-size: 24px; }
  .label--light .corner-mark { fill: var(--mark-light); }
  .label--sun .corner-mark { fill: var(--mark-dark); }
</style>
</head>
<body>
<main class="canvas">

  <!-- White variant -->
  <section class="label label--light">
    <svg viewBox="0 0 727 516" xmlns="http://www.w3.org/2000/svg">
      <defs>
        <linearGradient id="paper-light" x1="0" y1="0" x2="1" y2="1">
          <stop offset="0" stop-color="#fdf3f3"/>
          <stop offset="0.5" stop-color="#fbfcf7"/>
          <stop offset="1" stop-color="#eef7fc"/>
        </linearGradient>
        <linearGradient id="hex-fill" x1="0" y1="0" x2="1" y2="1">
          <stop offset="0" stop-color="#1c1512"/>
          <stop offset="0.55" stop-color="#070707"/>
          <stop offset="1" stop-color="#0d1a22"/>
        </linearGradient>
      </defs>
      <rect class="candy-pattern" width="727" height="516" fill="url(#paper-light)" role="img" aria-label="Lys mønsterflade med pastelfarvede slik og bolsjer"/>
      <polygon class="hex-frame" points="353,67 518,158 518,354 353,450 186,354 186,158" fill="none" stroke="var(--sun)" stroke-width="5"/>
      <polygon class="hex-panel" points="352,84 502,169 502,346 352,431 202,346 202,169" fill="url(#hex-fill)" stroke="var(--sun)" stroke-width="3" role="img" aria-label="Mørk flade med svage slikillustrationer"/>
      <text class="brand" x="350" y="158" text-anchor="middle">NORDA SWEETS</text>
      <text class="tagline" x="350" y="182" text-anchor="middle">Keep it Sweet &amp; Simple</text>
      <text class="title" x="353" y="235" text-anchor="middle">KARAMELLER</text>
      <line x1="233" y1="262" x2="300" y2="262" stroke="var(--white)" stroke-width="3"/>
      <line x1="409" y1="262" x2="475" y2="262" stroke="var(--white)" stroke-width="3"/>
      <text class="script" x="354" y="277" text-anchor="middle">med</text>
      <text class="title" x="354" y="321" text-anchor="middle">HAVSALT</text>
      <text class="copy" x="357" y="343" text-anchor="middle">Cool karameller der</text>
      <text class="copy" x="357" y="360" text-anchor="middle">Ikke klistrer I tænderne</text>
      <text class="copy" x="357" y="377" text-anchor="middle">Pjattet gode og</text>
      <text class="copy" x="357" y="394" text-anchor="middle">Imponerende</text>
      <text class="corner-mark" x="46" y="491">Reno</text>
      <text class="corner-mark" x="631" y="491">Reno</text>
    </svg>
  </section>

  <!-- Yellow variant -->
  <section class="label label--sun">
    <svg viewBox="0 0 727 516" xmlns="http://www.w3.org/2000/svg">
      <defs>
        <linearGradient id="paper-sun" x1="0" y1="0" x2="1" y2="1">
          <stop offset="0" stop-color="#fbbf0a"/>
          <stop offset="0.5" stop-color="#fdc800"/>
          <stop offset="1" stop-color="#f8bb08"/>
        </linearGradient>
        <linearGradient id="hex-fill-2" x1="0" y1="0" x2="1" y2="1">
          <stop offset="0" stop-color="#1c1512"/>
          <stop offset="0.55" stop-color="#070707"/>
          <stop offset="1" stop-color="#0d1a22"/>
        </linearGradient>
      </defs>
      <rect class="candy-pattern" width="727" height="516" fill="url(#paper-sun)" role="img" aria-label="Gul mønsterflade med slik og bolsjer i gule og orange toner"/>
      <polygon class="hex-frame" points="353,67 518,158 518,354 353,450 186,354 186,158" fill="var(--sun)" stroke="var(--white)" stroke-width="5"/>
      <polygon class="hex-panel" points="352,84 502,169 502,346 352,431 202,346 202,169" fill="url(#hex-fill-2)" role="img" aria-label="Mørk flade med svage slikillustrationer"/>
      <text class="brand" x="350" y="158" text-anchor="middle">NORDA SWEETS</text>
      <text class="tagline" x="350" y="182" text-anchor="middle">Keep it Sweet &amp; Simple</text>
      <text class="title" x="353" y="235" text-anchor="middle">KARAMELLER</text>
      <line x1="233" y1="262" x2="300" y2="262" stroke="var(--white)" stroke-width="3"/>
      <line x1="409" y1="262" x2="475" y2="262" stroke="var(--white)" stroke-width="3"/>
      <text class="script" x="354" y="277" text-anchor="middle">med</text>
      <text class="title" x="354" y="321" text-anchor="middle">HAVSALT</text>
      <text class="copy" x="357" y="343" text-anchor="middle">Cool karameller der</text>
      <text class="copy" x="357" y="360" text-anchor="middle">Ikke klistrer I tænderne</text>
      <text class="copy" x="357" y="377" text-anchor="middle">Pjattet gode og</text>
      <text class="copy" x="357" y="394" text-anchor="middle">Imponerende</text>
      <text class="corner-mark" x="46" y="491">Reno</text>
      <text class="corner-mark" x="631" y="491">Reno</text>
    </svg>
  </section>

</main>
</body>
</html>
```